Bao Lotus Menu Design Project

This project is pretty straight forward. You will be given 3 files which include the following:
1. Our proposed menu
2. Our Company logo
3. A sample menu on what we are looking for design wise

Your job is to create a visually pleasing menu that is simple, clean and fresh. Please refer to our home website for additional information. (www.baolotus-example.com) Must be in eps or equivalent format.

Target Market(s)

20s to 40s

Industry/Entity Type

It Company

Requirements
Must have
• Company log
Must be in EPS format

```html
<!DOCTYPE html>
<html lang="en">
<head>
<meta charset="utf-8">
<title>Bao Lotus Menu</title>
<link rel="stylesheet" href="https://fonts.googleapis.com/css2?family=EB+Garamond:ital@1&family=Roboto+Condensed:wght@500&family=Quicksand:wght@300&display=swap">
<style>
:root{
  --backdrop:#ecebe8;
  --orange:#f1602a;
  --orange-deep:#e24f1d;
  --rust:#b8501e;
  --ink:#151515;
  --grey-light:#eceded;
  --grey-mid:#a4a8ab;
  --grey-dark:#464c52;
  --beige:#e6d8c3;
  --white:#ffffff;
}
*{box-sizing:border-box;margin:0;padding:0}
html,body{width:1144px;height:1200px;overflow:hidden;background:var(--backdrop)}
.canvas{position:relative;width:1144px;height:1200px}

/* cover page */
.cover{position:absolute;left:61px;top:40px;width:668px;height:1101px;overflow:hidden;
  background:radial-gradient(ellipse 62% 40% at 52% 50%,var(--grey-light) 0%,#c4c7c9 45%,var(--grey-mid) 70%,var(--grey-dark) 100%);
  box-shadow:0 4px 14px rgba(0,0,0,.25)}
.cover-photo{position:absolute;left:0;top:0;width:668px;height:316px;
  background:
    radial-gradient(circle at 17% 6%,rgba(255,190,90,.85) 0,rgba(255,170,70,0) 7%),
    radial-gradient(circle at 36% 5%,rgba(255,180,80,.75) 0,rgba(255,170,70,0) 6%),
    radial-gradient(circle at 56% 5%,rgba(255,180,80,.7) 0,rgba(255,170,70,0) 5%),
    radial-gradient(ellipse 40% 18% at 80% 22%,rgba(70,110,120,.55) 0,rgba(70,110,120,0) 100%),
    radial-gradient(ellipse 30% 12% at 78% 82%,rgba(230,220,200,.35) 0,rgba(230,220,200,0) 100%),
    radial-gradient(ellipse 50% 40% at 8% 30%,rgba(150,90,30,.8) 0,rgba(150,90,30,0) 100%),
    linear-gradient(180deg,#3a2a1a 0%,#241a14 35%,#2e211a 60%,#1a1411 100%)}
.badge{position:absolute;border-radius:50%;background:radial-gradient(circle at 45% 35%,#ffffff 0%,#ececec 65%,#cfcfcf 100%);
  box-shadow:4px 6px 9px rgba(0,0,0,.35);display:flex;align-items:center;justify-content:center}
.badge-name{font-family:"Roboto Condensed",sans-serif;font-weight:500;color:#c5283a;letter-spacing:1px;white-space:nowrap}
.cover .badge{left:243px;top:234px;width:164px;height:164px}
.cover .badge-name{font-size:30px}
.tagline{position:absolute;font-family:"EB Garamond",serif;font-style:italic;white-space:nowrap;line-height:1}
.tagline-lead{left:163px;top:508px;font-size:29px;color:var(--ink)}
.tagline-main{left:117px;top:548px;font-size:64px;color:var(--rust);letter-spacing:6px}
.cover-dish{position:absolute;left:178px;top:690px;width:490px;height:411px;
  border-radius:180px 0 0 0 / 60px 0 0 0;
  background:
    radial-gradient(ellipse 22% 12% at 60% 30%,rgba(70,130,40,.9) 0,rgba(70,130,40,0) 100%),
    radial-gradient(ellipse 20% 14% at 45% 55%,rgba(80,140,45,.85) 0,rgba(80,140,45,0) 100%),
    radial-gradient(ellipse 25% 12% at 82% 62%,rgba(70,125,40,.85) 0,rgba(70,125,40,0) 100%),
    radial-gradient(ellipse 20% 14% at 30% 78%,rgba(60,110,35,.8) 0,rgba(60,110,35,0) 100%),
    radial-gradient(ellipse 60% 52% at 62% 62%,#4a2a22 0,#35201b 55%,rgba(53,32,27,0) 78%),
    linear-gradient(200deg,#ffffff 0%,#f2f2f2 20%,#d9d9d9 45%,#f5f5f5 75%,#ffffff 100%)}

/* menu index page */
.index{position:absolute;left:776px;top:40px;width:334px;height:1101px;background:var(--white);overflow:hidden;
  box-shadow:0 4px 14px rgba(0,0,0,.25)}
.index-header{position:absolute;left:0;top:0;width:334px;height:213px;overflow:hidden;
  background:radial-gradient(ellipse 60% 80% at 50% 30%,#ff7a3a 0%,var(--orange) 45%,var(--orange-deep) 100%)}
.index .badge{left:100px;top:62px;width:118px;height:118px}
.index .badge-name{font-size:21px}
.index-title{position:absolute;left:0;width:334px;top:148px;text-align:center;font-family:"Quicksand",sans-serif;font-weight:300;
  font-size:88px;line-height:1;color:rgba(255,255,255,.45)}
.sections{position:absolute;left:0;top:281px;width:334px;list-style:none}
.section{position:relative;height:63px;display:flex;align-items:center}
.section-name{position:absolute;left:22px;font-family:"Roboto Condensed",sans-serif;font-weight:500;font-size:20px;color:var(--ink);white-space:nowrap;letter-spacing:-.2px}
.section-photo{position:absolute;left:135px;top:4px;width:184px;height:55px;
  -webkit-mask-image:linear-gradient(90deg,transparent 0,#000 22%);mask-image:linear-gradient(90deg,transparent 0,#000 22%)}
.p1{background:radial-gradient(ellipse 30% 50% at 45% 55%,#f2ede2 0,rgba(242,237,226,0) 100%),radial-gradient(ellipse 30% 50% at 78% 40%,#efe8d8 0,rgba(239,232,216,0) 100%),linear-gradient(90deg,#e0d9c8,#c9bfa8)}
.p2{background:radial-gradient(ellipse 25% 45% at 40% 40%,#f1e6c8 0,rgba(241,230,200,0) 100%),radial-gradient(ellipse 25% 45% at 80% 55%,#e8d4a2 0,rgba(232,212,162,0) 100%),linear-gradient(90deg,#d6b47a,#a9773d)}
.p3{background:radial-gradient(ellipse 30% 50% at 45% 45%,#d98f84 0,rgba(217,143,132,0) 100%),radial-gradient(ellipse 20% 45% at 85% 55%,#e8dcc6 0,rgba(232,220,198,0) 100%),linear-gradient(90deg,#c77a68,#7e3b2f)}
.p4{background:radial-gradient(ellipse 25% 45% at 40% 50%,#b4572a 0,rgba(180,87,42,0) 100%),radial-gradient(ellipse 25% 45% at 78% 40%,#a84a22 0,rgba(168,74,34,0) 100%),linear-gradient(90deg,#6b2810,#4a180a)}
.p5{background:radial-gradient(ellipse 25% 45% at 35% 50%,#7a2a1c 0,rgba(122,42,28,0) 100%),radial-gradient(ellipse 28% 50% at 78% 45%,#b0604a 0,rgba(176,96,74,0) 100%),linear-gradient(90deg,#4a140e,#6a2418)}
.p6{background:radial-gradient(ellipse 25% 45% at 45% 30%,#ffffff 0,rgba(255,255,255,0) 100%),radial-gradient(ellipse 30% 45% at 80% 75%,#f4f2ee 0,rgba(244,242,238,0) 100%),linear-gradient(90deg,#dfe3ec,#c3cad9)}
.p7{background:radial-gradient(ellipse 20% 40% at 40% 40%,#f2b48a 0,rgba(242,180,138,0) 100%),radial-gradient(ellipse 20% 40% at 70% 65%,#f0a878 0,rgba(240,168,120,0) 100%),linear-gradient(90deg,#e18a5a,#b8461e)}
.p8{background:radial-gradient(ellipse 22% 40% at 40% 55%,#7a3a7a 0,rgba(122,58,122,0) 100%),radial-gradient(ellipse 18% 35% at 75% 35%,#c46a8a 0,rgba(196,106,138,0) 100%),radial-gradient(ellipse 14% 30% at 55% 25%,#5a8a2a 0,rgba(90,138,42,0) 100%),linear-gradient(90deg,#3a1a3a,#5a2a50)}
.p9{background:radial-gradient(ellipse 18% 35% at 55% 30%,#e8946a 0,rgba(232,148,106,0) 100%),radial-gradient(ellipse 30% 50% at 75% 60%,#eadcb0 0,rgba(234,220,176,0) 100%),linear-gradient(90deg,#d8c08a,#b4925a)}
.p10{background:radial-gradient(ellipse 25% 45% at 45% 55%,#c88a4a 0,rgba(200,138,74,0) 100%),radial-gradient(ellipse 15% 35% at 70% 40%,#4a7a2a 0,rgba(74,122,42,0) 100%),linear-gradient(90deg,#9a5f2c,#5a3418)}
.p11{background:radial-gradient(ellipse 18% 45% at 55% 45%,#3a1e16 0,rgba(58,30,22,0) 100%),radial-gradient(ellipse 15% 20% at 40% 85%,#c8283a 0,rgba(200,40,58,0) 100%),linear-gradient(90deg,#f4f2f0,#e8e2dc 70%,#f2eeea)}
.p12{background:radial-gradient(ellipse 30% 40% at 40% 25%,#f6f2ea 0,rgba(246,242,234,0) 100%),radial-gradient(ellipse 35% 50% at 75% 70%,#d98a2a 0,rgba(217,138,42,0) 100%),linear-gradient(90deg,#e6d2b2,#a8581a)}
.index-footer{position:absolute;left:0;top:1067px;width:334px;height:34px;background:var(--beige)}
.page-number{position:absolute;left:0;top:0;width:34px;height:34px;background:var(--orange);color:var(--white);
  font-family:"Roboto Condensed",sans-serif;font-size:20px;display:flex;align-items:center;justify-content:center}
</style>
</head>
<body>
<main class="canvas">
  <section class="cover">
    <div class="cover-photo" role="img" aria-label="Photo of the restaurant dining room with dark leather booths and warm pendant lights"></div>
    <div class="badge"><span class="badge-name">Bao Lotus</span></div>
    <p class="tagline tagline-lead">Experience the Art of</p>
    <p class="tagline tagline-main">Chinese Cuisine</p>
    <div class="cover-dish" role="img" aria-label="Photo of a white plate of stir-fried beef with green scallions"></div>
  </section>

  <section class="index">
    <header class="index-header">
      <div class="badge"><span class="badge-name">Bao Lotus</span></div>
      <div class="index-title">menu</div>
    </header>
    <ul class="sections">
      <li class="section"><span class="section-name">Dim Sum</span><div class="section-photo p1" role="img" aria-label="Photo of dumplings"></div></li>
      <li class="section"><span class="section-name">Salads</span><div class="section-photo p2" role="img" aria-label="Photo of a shredded salad"></div></li>
      <li class="section"><span class="section-name">Soup</span><div class="section-photo p3" role="img" aria-label="Photo of wonton soup with pork"></div></li>
      <li class="section"><span class="section-name">Chicken</span><div class="section-photo p4" role="img" aria-label="Photo of glazed chicken"></div></li>
      <li class="section"><span class="section-name">Beef / Pork</span><div class="section-photo p5" role="img" aria-label="Photo of roast pork slices"></div></li>
      <li class="section"><span class="section-name">Combination</span><div class="section-photo p6" role="img" aria-label="Photo of combination plates"></div></li>
      <li class="section"><span class="section-name">Seafood</span><div class="section-photo p7" role="img" aria-label="Photo of shrimp"></div></li>
      <li class="section"><span class="section-name">Vegetables</span><div class="section-photo p8" role="img" aria-label="Photo of eggplant stir-fry"></div></li>
      <li class="section"><span class="section-name">Rice &amp; Mushu</span><div class="section-photo p9" role="img" aria-label="Photo of shrimp fried rice"></div></li>
      <li class="section"><span class="section-name">Noodles</span><div class="section-photo p10" role="img" aria-label="Photo of chow mein noodles"></div></li>
      <li class="section"><span class="section-name">Desserts</span><div class="section-photo p11" role="img" aria-label="Photo of a chocolate cake dessert"></div></li>
      <li class="section"><span class="section-name">Beverages</span><div class="section-photo p12" role="img" aria-label="Photo of an iced drink"></div></li>
    </ul>
    <footer class="index-footer"><span class="page-number">1</span></footer>
  </section>
</main>
</body>
</html>
```